We need a wordpress website design (preferably using canvas theme) for a new company called Copper Ridge Analytics (CRA). CRA is a business to business site that provides information, news, and data about the medical marijuana industry. The site will have a home page/dashboard that highlights the top news, featured companies, featured people, and featured reports. The site will also have profile pages that contain detailed information about companies, people, events, and states (regulations). The site will also have a woo commerce store for reports and data extracts.
Note: In general, we are using Calibri for logo and header fonts. A readable sans serif for text. Copper Ridge Blue: RGB: 3 56 121 HEX: 033879
We can also use complimentary green accents, and shades of blue and grey around it as accent.
Updates

Target Market(s)

- Professional, entrepreneurial men 29-55 years old. They are young high net worth investors, lawyers, entrepreneurs and in the financial sector – or they strive to be there.
- They read Brisk Venture, Harbor Lane Gazette, Capital Markets Weekly, hempledgerwire.example (they wish it were better). They visit the site sproutlo.example
- they follow us on twitter and facebook.

Industry/Entity Type

Medical

Font styles to use
Sans Serif

Colors
0255a3
acd036
3176b5
85acd3
eaf1f7

Requirements
Must have
• Widgets on the home page may include stock feeds, as well as groups of information such as events and featured people.

User must have ability to see featured reports including cover art and brief (one line) summary so they can go purchase them in the store. Once in the store, they can preview a longer abstract (~50-200 words). User will want to know length of report in pages before they buy
Nice to have
• Lots of images throughout the site, for instance images that are associated with each report. those images may be the cover art. Also images associated with the people, events, etc. These will typically be profile pics and company logos.
Should not have
• Although this is a medical marijuana site, we do not want to have graphics, images, or icons that show marijuana leaves or flowers.

```html
<!DOCTYPE html>
<html lang="en">
<head>
<meta charset="utf-8">
<title>Copper Ridge Analytics — Home</title>
<link rel="stylesheet" href="https://fonts.googleapis.com/css2?family=Carlito:wght@400;700&family=Open+Sans:wght@400;600&display=swap">
<style>
:root{
  --brand-blue:#033879;
  --bar-blue:#163f7f;
  --link-blue:#1a4f8b;
  --accent-red:#e04a3a;
  --text-dark:#333;
  --text-mid:#666;
  --text-light:#999;
  --line:#d8d8d8;
  --band-grey:#f2f2f2;
  --side-grey:#e4e6e9;
  --foot-grey:#e9ecef;
  --ad-grey:#a3adb6;
  --white:#fff;
}
*{box-sizing:border-box;margin:0;padding:0}
html,body{width:1200px;height:2308px;overflow:hidden}
body{position:relative;background:var(--white);font-family:"Open Sans",Arial,sans-serif;color:var(--text-dark);font-size:12px}
.abs{position:absolute}
.heading{font-family:"Carlito","Calibri",sans-serif}
ul{list-style:none}

/* top bar */
.top-bar{left:0;top:0;width:1200px;height:25px;background:var(--bar-blue);color:var(--white);font-size:10px;text-align:right;padding:6px 28px 0 0;letter-spacing:.3px}
.top-bar b{font-size:13px;margin-left:3px}

/* header */
.logo{left:80px;top:56px;display:flex;align-items:center;gap:12px}
.logo-dot{width:44px;height:44px;border-radius:50%;background:var(--brand-blue)}
.logo-name{font-family:"Carlito","Calibri",sans-serif;font-size:36px;color:var(--brand-blue);font-weight:400}
.account-links{left:751px;top:57px;font-size:11px;line-height:27px;color:var(--text-dark)}
.account-links li{display:flex;align-items:center;gap:12px}
.account-links i{width:13px;height:11px;background:var(--accent-red);display:block}
.social{left:1013px;top:44px;display:flex;gap:3px}
.social span{width:31px;height:31px;background:var(--brand-blue);display:block}
.search{left:892px;top:87px;width:214px;height:22px;border:1px solid #ccc;background:#fafafa;font-size:11px;color:#555;padding:3px 8px;display:flex;justify-content:space-between}
.search i{width:18px;height:18px;margin:-2px -7px 0 0;background:#ccc;display:block}

/* nav */
.main-nav{left:0;top:126px;width:1200px;height:50px;background:var(--accent-red);display:flex;font-size:15px;color:var(--white)}
.main-nav li{position:absolute;top:0;height:50px;line-height:50px}
.main-nav .current{background:var(--white);color:var(--text-dark);border-top:3px solid #ccc;line-height:45px;width:67px;text-align:center}

/* top news */
.news-band{left:0;top:176px;width:1200px;height:449px;background:var(--band-grey)}
.section-title{font-size:28px;color:var(--link-blue)}
.news-title{left:92px;top:210px}
.news-strip{left:0;top:260px;width:1200px;height:363px;background:var(--white);border-top:1px solid var(--line);border-bottom:1px solid var(--line)}
.circle-arrow{width:24px;height:24px;border:2px solid #bbb;border-radius:50%}
.news-card{top:287px;width:212px}
.photo{display:block;background:linear-gradient(135deg,#8a7a5a,#c9b892 55%,#6d6148)}
.news-card .photo{height:151px}
.news-card h3{font-size:13px;font-weight:600;color:var(--brand-blue);margin:9px 10px 4px;line-height:17px}
.meta{font-size:10px;color:#5575a5;margin:0 10px;line-height:17px}
.meta span{color:var(--text-mid)}
.summary{font-size:11px;color:var(--text-dark);margin:4px 10px 0;line-height:15px}
.news-foot{position:absolute;top:293px;left:0;width:212px;border-top:1px solid var(--line);padding-top:8px;font-size:10px;display:flex;justify-content:flex-end;gap:10px;padding-right:10px}
.news-foot .more{color:var(--accent-red)}
.news-foot i{width:11px;height:8px;background:#bbb;border-radius:50%;display:inline-block;margin-left:4px}

/* featured blocks */
.feat-head{left:94px;display:flex;align-items:center;gap:20px}
.feat-head i{width:24px;height:26px;background:var(--brand-blue);display:block}
.feat-head .section-title{font-size:27px}
.pager{left:786px;display:flex;gap:4px}
.feat-box{left:92px;width:728px;height:204px;border:1px solid var(--line);background:var(--white);box-shadow:0 1px 3px rgba(0,0,0,.08)}
.feat-item{position:absolute;top:10px;width:134px}
.feat-item .photo{height:128px}
.feat-item p{font-size:11px;line-height:16px;margin-top:6px;color:var(--text-dark)}
.feat-item small{font-size:11px;color:var(--text-light)}
.people{background:linear-gradient(160deg,#4a3b33,#c99a7e 50%,#3a2f2a)}
.company{background:linear-gradient(160deg,#7d8794,#d6cfc6 50%,#56606e)}
.report{background:linear-gradient(160deg,#6f8fb0,#e3e8ee 50%,#8b9db2)}

/* link lists */
.link-box{top:1613px;width:349px;height:332px;border:1px solid var(--line);background:var(--white)}
.link-box h2{height:50px;line-height:50px;padding-left:18px;color:var(--white);font-size:28px;font-weight:400}
.red h2{background:var(--accent-red)}
.blue h2{background:var(--bar-blue)}
.link-box ul{padding:18px 20px 0 30px}
.link-box li{font-size:11px;line-height:17px;color:var(--brand-blue);margin-bottom:14px;position:relative}
.link-box li:before{content:"";position:absolute;left:-14px;top:7px;width:4px;height:4px;background:var(--accent-red)}
.link-box li span{color:var(--text-light)}
.view-all{position:absolute;right:24px;bottom:20px;font-size:10px;color:var(--accent-red)}

/* sidebar */
.sidebar{left:845px;top:652px;width:265px;height:1294px;background:var(--side-grey);border:1px solid var(--line)}
.tabs{display:flex;height:40px;font-size:11px}
.tabs li{flex:1;text-align:center;line-height:40px}
.tabs .active{background:var(--accent-red);color:var(--white);flex:0 0 132px}
.tabs li:last-child{background:var(--white)}
.side-post{position:absolute;left:14px;width:236px}
.side-post .photo{height:126px}
.side-post p{font-size:11px;line-height:15px;margin-top:8px}
.ad{position:absolute;left:14px;width:236px;height:218px;background:var(--ad-grey);color:var(--white)}
.ad small{font-size:10px;position:absolute;left:12px;top:10px}
.ad strong{font-family:"Carlito","Calibri",sans-serif;font-weight:400;font-size:42px;position:absolute;left:0;right:0;text-align:center;top:82px}
.newsletter-title{position:absolute;left:14px;top:1096px;font-size:28px;line-height:34px;color:var(--text-dark);font-weight:400}
.newsletter{position:absolute;left:14px;top:1140px;width:236px;height:140px;background:var(--white);border:1px solid var(--line);padding:14px 14px}
.newsletter p{font-size:11px}
.newsletter .field{margin-top:26px;width:206px;height:27px;border:1px solid #ccc;font-size:11px;padding:5px 8px;background:#f8f8f8}
.newsletter .btn{display:inline-block;margin-top:10px;background:var(--accent-red);color:var(--white);font-size:11px;padding:4px 18px;letter-spacing:.3px}

/* footer */
.footer{left:0;top:1966px;width:1200px;height:275px;background:var(--foot-grey);border-top:1px solid var(--line)}
.foot-col{position:absolute;top:26px}
.foot-col h4{font-family:"Carlito","Calibri",sans-serif;font-weight:400;font-size:26px;color:var(--brand-blue);margin-bottom:18px}
.foot-col li{font-size:11px;line-height:22px}
.contact li{display:flex;gap:16px;line-height:16px;margin-bottom:18px;align-items:flex-start}
.contact svg{flex:0 0 16px}
.bottom-bar{left:0;top:2241px;width:1200px;height:67px;background:var(--bar-blue);color:var(--white)}
.copyright{position:absolute;left:120px;top:25px;font-size:11px}
.foot-brand{position:absolute;right:74px;top:18px;display:flex;align-items:center;gap:10px;font-family:"Carlito","Calibri",sans-serif;font-size:24px}
.foot-brand i{width:22px;height:22px;background:var(--white);display:block}
</style>
</head>
<body>

<div class="abs top-bar">VIEW LARGER TEXT <b>A</b> <b>A</b></div>

<header>
  <div class="abs logo"><span class="logo-dot"></span><span class="logo-name">Copper Ridge Analytics</span></div>
  <ul class="abs account-links"><li><i></i>View Cart</li><li><i></i>My Account</li></ul>
  <div class="abs social" aria-label="Social links"><span></span><span></span><span></span></div>
  <div class="abs search">search...<i></i></div>
</header>

<nav>
  <ul class="abs main-nav">
    <li class="current" style="left:92px">Home</li>
    <li style="left:222px">Profile</li>
    <li style="left:329px">Store</li>
    <li style="left:418px">About us</li>
    <li style="left:529px">Contact us</li>
  </ul>
</nav>

<section>
  <div class="abs news-band"></div>
  <h1 class="abs heading section-title news-title" style="font-weight:400">Top Marijuana Industry News</h1>
  <div class="abs news-strip"></div>
  <div class="abs circle-arrow" style="left:93px;top:349px"><svg width="20" height="20"><path d="M12 5 L7 10 L12 15" fill="none" stroke="#bbb" stroke-width="2"/></svg></div>
  <div class="abs circle-arrow" style="left:1081px;top:349px"><svg width="20" height="20"><path d="M8 5 L13 10 L8 15" fill="none" stroke="#bbb" stroke-width="2"/></svg></div>

  <article class="abs news-card" style="left:130px">
    <div class="photo" role="img" aria-label="News photo"></div>
    <h3>Lorem ipsum dolor sit amet, consectetur</h3>
    <p class="meta">Posted in: <span>Health</span><br>Posted on: <span>13-10-2014</span></p>
    <p class="summary">Quisque placerat et orci ac lacinia. Aenean orci est, egestas at posuere facilisi</p>
    <div class="news-foot"><span>2 comments<i></i></span><span class="more">Read more</span></div>
  </article>
  <article class="abs news-card" style="left:371px">
    <div class="photo" role="img" aria-label="News photo" style="background:linear-gradient(135deg,#3e4a2e,#8b8a60 55%,#2d3324)"></div>
    <h3>Lorem ipsum dolor sit amet, consectetur</h3>
    <p class="meta">Posted in: <span>Health</span><br>Posted on: <span>13-10-2014</span></p>
    <p class="summary">Quisque placerat et orci ac lacinia. Aenean orci est, egestas at posuere facilisi</p>
    <div class="news-foot"><span>2 comments<i></i></span><span class="more">Read more</span></div>
  </article>
  <article class="abs news-card" style="left:613px">
    <div class="photo" role="img" aria-label="News photo" style="background:linear-gradient(135deg,#5b5d3d,#a69c70 55%,#4b4a32)"></div>
    <h3>Lorem ipsum dolor sit amet, consectetur</h3>
    <p class="meta">Posted in: <span>Health</span><br>Posted on: <span>13-10-2014</span></p>
    <p class="summary">Quisque placerat et orci ac lacinia. Aenean orci est, egestas at posuere facilisi</p>
    <div class="news-foot"><span>2 comments<i></i></span><span class="more">Read more</span></div>
  </article>
  <article class="abs news-card" style="left:852px">
    <div class="photo" role="img" aria-label="News photo" style="background:linear-gradient(135deg,#6b4a3a,#a78a74 55%,#3f2e27)"></div>
    <h3>Lorem ipsum dolor sit amet, consectetur</h3>
    <p class="meta">Posted in: <span>Health</span><br>Posted on: <span>13-10-2014</span></p>
    <p class="summary">Quisque placerat et orci ac lacinia. Aenean orci est, egestas at posuere facilisi</p>
    <div class="news-foot"><span>2 comments<i></i></span><span class="more">Read more</span></div>
  </article>
</section>

<!-- featured companies -->
<section>
  <div class="abs feat-head" style="top:676px"><i></i><h2 class="heading section-title" style="font-weight:400">Featured Companies</h2></div>
  <svg class="abs pager" style="top:693px" width="34" height="14"><path d="M10 2 L4 7 L10 12 M24 2 L30 7 L24 12" fill="none" stroke="#aaa" stroke-width="2"/></svg>
  <div class="abs feat-box" style="top:726px;height:206px">
    <div class="feat-item" style="left:10px"><div class="photo company" role="img" aria-label="Company photo"></div><p>Quisque placerat et orci ac lacinia.</p><small>(Lorem ipsum)</small></div>
    <div class="feat-item" style="left:152px"><div class="photo company" role="img" aria-label="Company photo"></div><p>Quisque placerat et orci ac lacinia.</p><small>(Lorem ipsum)</small></div>
    <div class="feat-item" style="left:295px"><div class="photo company" role="img" aria-label="Company photo"></div><p>Quisque placerat et orci ac lacinia.</p><small>(Lorem ipsum)</small></div>
    <div class="feat-item" style="left:438px"><div class="photo company" role="img" aria-label="Company photo"></div><p>Quisque placerat et orci ac lacinia.</p><small>(Lorem ipsum)</small></div>
    <div class="feat-item" style="left:580px"><div class="photo company" role="img" aria-label="Company photo"></div><p>Quisque placerat et orci ac lacinia.</p><small>(Lorem ipsum)</small></div>
  </div>
</section>

<!-- featured people -->
<section>
  <div class="abs feat-head" style="top:989px"><i></i><h2 class="heading section-title" style="font-weight:400">Featured People</h2></div>
  <svg class="abs pager" style="top:1016px" width="34" height="14"><path d="M10 2 L4 7 L10 12 M24 2 L30 7 L24 12" fill="none" stroke="#aaa" stroke-width="2"/></svg>
  <div class="abs feat-box" style="top:1040px">
    <div class="feat-item" style="left:10px"><div class="photo people" role="img" aria-label="Profile portrait"></div><p>Quisque placerat et orci ac lacinia.</p><small>(Lorem ipsum)</small></div>
    <div class="feat-item" style="left:152px"><div class="photo people" role="img" aria-label="Profile portrait"></div><p>Quisque placerat et orci ac lacinia.</p><small>(Lorem ipsum)</small></div>
    <div class="feat-item" style="left:295px"><div class="photo people" role="img" aria-label="Profile portrait"></div><p>Quisque placerat et orci ac lacinia.</p><small>(Lorem ipsum)</small></div>
    <div class="feat-item" style="left:438px"><div class="photo people" role="img" aria-label="Profile portrait"></div><p>Quisque placerat et orci ac lacinia.</p><small>(Lorem ipsum)</small></div>
    <div class="feat-item" style="left:580px"><div class="photo people" role="img" aria-label="Profile portrait"></div><p>Quisque placerat et orci ac lacinia.</p><small>(Lorem ipsum)</small></div>
  </div>
</section>

<!-- featured reports -->
<section>
  <div class="abs feat-head" style="top:1302px"><i></i><h2 class="heading section-title" style="font-weight:400">Featured Reports</h2></div>
  <svg class="abs pager" style="top:1329px" width="34" height="14"><path d="M10 2 L4 7 L10 12 M24 2 L30 7 L24 12" fill="none" stroke="#aaa" stroke-width="2"/></svg>
  <div class="abs feat-box" style="top:1353px">
    <div class="feat-item" style="left:10px"><div class="photo report" role="img" aria-label="Report cover art"></div><p>Quisque placerat et orci ac lacinia.</p><small>(Lorem ipsum)</small></div>
    <div class="feat-item" style="left:152px"><div class="photo report" role="img" aria-label="Report cover art"></div><p>Quisque placerat et orci ac lacinia.</p><small>(Lorem ipsum)</small></div>
    <div class="feat-item" style="left:295px"><div class="photo report" role="img" aria-label="Report cover art"></div><p>Quisque placerat et orci ac lacinia.</p><small>(Lorem ipsum)</small></div>
    <div class="feat-item" style="left:438px"><div class="photo report" role="img" aria-label="Report cover art"></div><p>Quisque placerat et orci ac lacinia.</p><small>(Lorem ipsum)</small></div>
    <div class="feat-item" style="left:580px"><div class="photo report" role="img" aria-label="Report cover art"></div><p>Quisque placerat et orci ac lacinia.</p><small>(Lorem ipsum)</small></div>
  </div>
</section>

<!-- link lists -->
<section class="abs link-box red" style="left:92px">
  <h2 class="heading">Also on the Web</h2>
  <ul>
    <li>Quisque placerat et orci ac lacinia. <span>[ ]</span></li>
    <li>Aenean orci est, egestas at posuere facilisis, rutrum lobortis ipsum. <span>[ ]</span></li>
    <li>Lorem ipsum dolor sit amet, consectetur adipiscing elit. Duis at odio aliquet <span>[ ]</span></li>
    <li>Consectetur adipiscing elit. <span>[ ]</span></li>
    <li>Lorem ipsum dolor sit amet, consectetur adipiscing elit. Duis at odio aliquet <span>[ ]</span></li>
  </ul>
  <span class="view-all">&gt; View All</span>
</section>
<section class="abs link-box blue" style="left:470px">
  <h2 class="heading">More From Copper Ridge</h2>
  <ul>
    <li>Quisque placerat et orci ac lacinia. <span>[ ]</span></li>
    <li>Aenean orci est, egestas at posuere facilisis, rutrum lobortis ipsum. <span>[ ]</span></li>
    <li>Lorem ipsum dolor sit amet, consectetur adipiscing elit. Duis at odio aliquet <span>[ ]</span></li>
    <li>Consectetur adipiscing elit. <span>[ ]</span></li>
    <li>Aenean orci est, egestas at posuere facilisis, rutrum lobortis ipsum. <span>[ ]</span></li>
  </ul>
  <span class="view-all">&gt; View All</span>
</section>

<!-- sidebar -->
<aside class="abs sidebar">
  <ul class="tabs"><li class="active">MOST POPULAR</li><li>FEATURED</li></ul>
  <div class="side-post" style="top:55px"><div class="photo company" role="img" aria-label="Group business photo"></div><p>Quisque placerat et orci ac lacinia. Aenean orci est, egestas at posuere facilisi</p></div>
  <div class="side-post" style="top:246px"><div class="photo" role="img" aria-label="Business portrait" style="background:linear-gradient(135deg,#d8dde3,#f2f2f2 50%,#9aa7b4)"></div><p>Quisque placerat et orci ac lacinia. Aenean orci est, egestas at posuere facilisi</p></div>
  <div class="side-post" style="top:439px"><div class="photo" role="img" aria-label="Storefront photo" style="background:linear-gradient(135deg,#4a2e20,#b48a5c 50%,#5a3d2a)"></div><p>Quisque placerat et orci ac lacinia. Aenean orci est, egestas at posuere facilisi</p></div>
  <div class="ad" style="top:634px"><small>Advertisement</small><strong>AD HERE</strong></div>
  <div class="ad" style="top:864px"><small>Advertisement</small><strong>AD HERE</strong></div>
  <h3 class="heading newsletter-title">Newsletter</h3>
  <div class="newsletter">
    <p>Quisque placerat et orci ac lacinia.</p>
    <div class="field">Email Address</div>
    <span class="btn">SUBSCRIBE</span>
  </div>
</aside>

<footer>
  <div class="abs footer">
    <div class="foot-col" style="left:109px"><h4>Quick Links</h4>
      <ul><li>Home</li><li>About Copper Ridge</li><li>News</li><li>Companies</li><li>People</li><li>Reports</li><li>Shop</li></ul></div>
    <div class="foot-col" style="left:350px"><h4>Important Links</h4>
      <ul><li>Vestibulum iaculis</li><li>Lacinia est</li><li>Proin dictum</li><li>Elementum velit</li><li>Consequat ante</li><li>Lorem ipsum dolor</li></ul></div>
    <div class="foot-col" style="left:592px"><h4>Important Links</h4>
      <ul><li>Vestibulum iaculis</li><li>Lacinia est</li><li>Proin dictum</li><li>Elementum velit</li><li>Consequat ante</li><li>Lorem ipsum dolor</li></ul></div>
    <div class="foot-col contact" style="left:841px"><h4>Contact Information</h4>
      <ul>
        <li><svg width="16" height="18" viewBox="0 0 16 18"><path d="M8 1a6 6 0 0 0-6 6c0 4.5 6 10 6 10s6-5.5 6-10a6 6 0 0 0-6-6z" fill="#e04a3a"/><circle cx="8" cy="7" r="2.2" fill="#fff"/></svg><span>copperridgeanalytics.example (OTC: CRAN)<br>4120 Quarry Lane #208<br>Reno, NV 89501</span></li>
        <li><svg width="16" height="16" viewBox="0 0 16 16"><path d="M3 1l3 3-1.5 2c1 2 3 4 5 5l2-1.5 3 3-2 2C7 14 2 9 1 3z" fill="#e04a3a"/></svg><span>Phone: (555) 014-2290</span></li>
        <li><svg width="16" height="16" viewBox="0 0 16 16"><rect x="1" y="5" width="14" height="9" fill="#e04a3a"/><rect x="4" y="1" width="8" height="5" fill="#e04a3a"/><rect x="4" y="9" width="8" height="3" fill="#fff"/></svg><span>Fax: (555) 016-7730</span></li>
      </ul></div>
  </div>
  <div class="abs bottom-bar">
    <span class="copyright">Copyright © 2014 copperridgeanalytics.example</span>
    <span class="foot-brand"><i></i>Copper Ridge Inc</span>
  </div>
</footer>

</body>
</html>
```